The Brightwater Compass Business Card

We need an attractive business card with the logo that we bought from ArtVantly last year.
Our mission is to contribute to change the way today's leaders manage business companies bringing value to the workplace and helping them to build a new model of creating wealth.
Our logo is clear about our values : we seek Positive Change through People and are convinced that the pursuit of individual well-being and the chase of economic results can converge with the right management.
Management Consulting
Corinne Fabrelle
+34 612 98 70 31
corinne.fabrelle@thebrightwatercompass-mail.net
www.thebrightwatercompass-mail.net

```html
<!DOCTYPE html>
<html lang="en">
<head>
<meta charset="utf-8">
<title>The Brightwater Compass – Business Card</title>
<link rel="stylesheet" href="https://fonts.googleapis.com/css2?family=Mulish:wght@400;600&display=swap">
<style>
  :root {
    --backdrop: #1f1f1f;
    --card-white: #ffffff;
    --teal: #0e8580;
    --teal-soft: #5a9e9b;
    --ink-grey: #6b6b6b;
    --white: #ffffff;
  }
  * { margin: 0; padding: 0; box-sizing: border-box; }
  html, body {
    width: 1200px; height: 864px; overflow: hidden;
    background: var(--backdrop);
    font-family: "Mulish", sans-serif;
  }
  .stage { position: relative; width: 1200px; height: 864px; }
  .card {
    position: absolute; top: 312px;
    width: 420px; height: 240px;
    border-radius: 11px; overflow: hidden;
  }
  .card--front { left: 174px; background: var(--card-white); }
  .card--back { left: 606px; background: var(--teal); }

  .brand-name {
    position: absolute; font-size: 16px; font-weight: 600;
    letter-spacing: 0.3px; white-space: nowrap; line-height: 1.2;
  }
  .card--front .brand-name { left: 22px; top: 28px; color: var(--teal); z-index: 1; }
  .card--back .brand-name {
    left: 176px; width: 226px; top: 186px;
    color: var(--white); text-align: center; z-index: 1;
  }

  .tree-art { position: absolute; }
  .tree-art--front {
    left: 244px; top: 18px; width: 176px; height: 204px;
    border-radius: 90px 0 0 90px;
    background: radial-gradient(ellipse at 60% 50%, rgba(14,133,128,0.55), rgba(90,158,155,0.25) 70%, rgba(90,158,155,0) 100%);
  }
  .tree-art--back {
    left: 0; top: 16px; width: 214px; height: 224px;
    border-radius: 0 110px 0 0;
    background: radial-gradient(ellipse at 35% 55%, rgba(255,255,255,0.14), rgba(255,255,255,0.04) 70%, rgba(255,255,255,0) 100%);
  }

  .person { position: absolute; left: 21px; top: 132px; }
  .person__name { font-size: 15px; font-weight: 600; color: var(--teal); line-height: 1.2; }
  .person__role { font-size: 11px; color: var(--ink-grey); line-height: 1.3; }

  .contacts { position: absolute; left: 21px; top: 180px; list-style: none; z-index: 1; }
  .contacts li {
    display: flex; align-items: center; gap: 5px;
    font-size: 10.5px; color: var(--ink-grey); line-height: 14px; white-space: nowrap;
  }
  .contacts svg { width: 9px; height: 9px; fill: var(--ink-grey); flex: none; }
</style>
</head>
<body>
<main class="stage">
  <section class="card card--front" aria-label="Business card front">
    <div class="tree-art tree-art--front" role="img" aria-label="Teal tree illustration with leafy branches shaped like people"></div>
    <div class="brand-name">The Brightwater Compass</div>
    <div class="person">
      <p class="person__name">Corinne Fabrelle</p>
      <p class="person__role">President</p>
    </div>
    <ul class="contacts">
      <li>
        <svg viewBox="0 0 10 10" aria-hidden="true"><path d="M2 0.5 L3.6 2.6 L2.6 3.6 Q3.6 6 6.4 7.4 L7.4 6.4 L9.5 8 L8.2 9.5 Q4 9 0.5 1.8 Z"/></svg>
        +34 612 98 70 31
      </li>
      <li>
        <svg viewBox="0 0 10 10" aria-hidden="true"><path d="M0.5 2 H9.5 V8 H0.5 Z M1.2 2.6 L5 5.4 L8.8 2.6" stroke="#fff" stroke-width="0.7"/></svg>
        corinne.fabrelle@thebrightwatercompass-mail.net
      </li>
      <li>
        <svg viewBox="0 0 10 10" aria-hidden="true"><circle cx="5" cy="5" r="4.5"/><path d="M0.5 5 H9.5 M5 0.5 V9.5 M5 0.5 Q2 5 5 9.5 M5 0.5 Q8 5 5 9.5" stroke="#fff" stroke-width="0.6" fill="none"/></svg>
        www.thebrightwatercompass-mail.net
      </li>
    </ul>
  </section>

  <section class="card card--back" aria-label="Business card back">
    <div class="tree-art tree-art--back" role="img" aria-label="Faint tone-on-tone tree illustration"></div>
    <div class="brand-name">The Brightwater Compass</div>
  </section>
</main>
</body>
</html>
```